Start up Dialysis Clinic needs its first website - Velmora Health

Create a visually appealing and user-friendly website for Velmora Health, a dialysis clinic located in Mt. Irvine, Tobago. The website should effectively communicate our services to local, regional, and international patients, providing essential information and fostering trust and engagement..
Key Goals:

1. Informative: Provide comprehensive information about our services, facility, and team.
2. User-Friendly: Ensure the website is easy to navigate, with a clear structure and accessible content.
3. Engaging: Create a visually appealing design that reflects the professionalism and care of Velmora Health.
4. Responsive: Ensure the website is fully responsive and performs well on all devices, including desktops, tablets, and smartphones.
5. Trust-Building: Include testimonials, credentials, and patient resources to build trust with potential patients.
Scope of Work:

1. Home Page: An inviting and informative landing page that provides an overview of our clinic, mission, and services. Include a call to action for more information and contact details.
2. About Us: A detailed page about Velmora Health, including our mission, vision, team, and facility tour.
3. Services: A comprehensive page describing the dialysis services we offer, including Hemodialysis, Peritoneal Dialysis, and Home Hemodialysis.
4. Patient Information: A resourceful section with guides for new patients, FAQs, insurance and billing information, and downloadable forms.
5. Resources: Educational content about kidney health, dialysis options, diet and nutrition tips, and support groups.
6. Contact Us: A contact page with our address, phone number, email, office hours, a contact form, and a map.

```html
<!DOCTYPE html>
<html lang="en">
<head>
<meta charset="utf-8">
<title>Velmora Health — Dialysis Clinic</title>
<link href="https://fonts.googleapis.com/css2?family=Inter:wght@400;500;600;700;800&display=swap" rel="stylesheet">
<style>
:root{
  --blue:#2e6cb5;
  --steel:#3f7ea6;
  --green:#5e9b3f;
  --green-2:#6aa548;
  --band-blue:#4a80ad;
  --testi-bg:#4f83b6;
  --ink:#2b2b2b;
  --muted:#555;
  --light:#f3f4f6;
  --footer:#1b1b1b;
  --white:#fff;
}
*{box-sizing:border-box;margin:0;padding:0}
html,body{width:1200px;height:3562px;overflow:hidden}
body{font-family:'Inter',Arial,sans-serif;color:var(--ink);background:var(--white);position:relative}
.abs{position:absolute}
.btn{position:absolute;display:flex;align-items:center;justify-content:center;color:var(--white);font-weight:700;text-transform:uppercase;background:linear-gradient(90deg,var(--steel),var(--green-2))}

/* header */
.site-header{position:absolute;left:0;top:0;width:1200px;height:151px;background:var(--white)}
.brand{position:absolute;left:131px;top:44px;display:flex;align-items:center;gap:10px}
.brand-mark{width:40px;height:40px;background:var(--blue)}
.brand-name{font-weight:800;font-size:24px;color:var(--blue);line-height:1;letter-spacing:.5px;white-space:nowrap}
.contact-chip{position:absolute;top:32px;display:flex;gap:12px;align-items:center}
.chip-icon{width:32px;height:32px;border-radius:50%;background:var(--steel);display:flex;align-items:center;justify-content:center}
.chip-label{font-size:12px;color:#333}
.chip-value{font-size:18px;font-weight:500;color:var(--blue);margin-top:2px}
.main-nav{position:absolute;top:93px;left:419px;display:flex;font-size:14.5px;color:#222}
.main-nav span{height:33px;display:flex;align-items:center}
.main-nav .active{background:var(--blue);color:var(--white);padding:0 11px}

/* hero */
.hero{position:absolute;left:0;top:151px;width:1200px;height:536px;background:linear-gradient(100deg,#e8f2f8 0%,#d6e7f1 40%,#c7dbe8 60%,#eef4f8 100%)}
.hero-title{position:absolute;left:130px;top:112px;font-size:47px;font-weight:800;line-height:55px;color:var(--blue);text-transform:uppercase}
.hero-text{position:absolute;left:131px;top:292px;font-size:19px;line-height:32px;color:#222}
.hero .btn{left:134px;top:382px;width:126px;height:44px;font-size:15px}
.dots{position:absolute;left:565px;top:490px;display:flex;gap:9px}
.dots i{width:11px;height:11px;border-radius:50%;background:var(--blue)}
.dots i:first-child{background:var(--green-2)}

/* mission */
.mission{position:absolute;left:0;top:687px;width:1200px;height:175px;background:linear-gradient(90deg,var(--band-blue) 0%,#4f86a7 45%,var(--green-2) 100%);overflow:hidden}
.mission-title{position:absolute;left:227px;top:68px;font-size:30px;font-weight:700;color:var(--white)}
.mission-rule{position:absolute;left:471px;top:39px;width:2px;height:94px;background:var(--white)}
.mission-text{position:absolute;left:522px;top:41px;width:530px;font-size:15.5px;line-height:22.5px;color:var(--white)}

/* welcome */
.welcome-media{position:absolute;left:131px;top:920px;width:378px;height:393px;background:linear-gradient(135deg,#78b48e,#6fa6c6 55%,#82bfae)}
.welcome-kicker{position:absolute;left:572px;top:912px;font-size:28px;font-weight:700;color:var(--blue)}
.welcome-title{position:absolute;left:572px;top:950px;font-size:38px;font-weight:700;color:var(--blue)}
.welcome-title b{color:var(--green);font-weight:700}
.rule{position:absolute;height:3px;background:var(--blue)}
.welcome-text{position:absolute;left:574px;top:1055px;width:488px;font-size:13.8px;line-height:22.4px;color:#333;text-align:justify}
.welcome .btn{left:574px;top:1267px;width:125px;height:43px;font-size:15px}

/* services */
.services{position:absolute;left:0;top:1374px;width:1200px;height:730px;background:repeating-linear-gradient(45deg,#f5f5f5 0 18px,#efefef 18px 36px)}
.section-title{position:absolute;font-size:36px;font-weight:700;color:var(--blue)}
.section-title b{color:var(--green);font-weight:700}
.service-card{position:absolute;top:175px;width:297px;height:485px;filter:drop-shadow(0 6px 10px rgba(0,0,0,.08))}
.service-card svg{position:absolute;left:0;top:0}
.service-photo{position:absolute;left:0;top:0;width:297px;height:227px}
.service-icon{position:absolute;left:194px;top:177px;width:58px;height:58px;border-radius:50%;background:linear-gradient(135deg,var(--steel),var(--green-2));border:3px solid var(--white);display:flex;align-items:center;justify-content:center}
.service-name{position:absolute;left:29px;top:262px;font-size:18px;font-weight:700;color:var(--blue)}
.service-text{position:absolute;left:29px;top:294px;width:245px;font-size:12.5px;line-height:17.5px;color:#444}
.service-card .btn{left:29px;top:379px;width:97px;height:32px;font-size:11.5px}

/* testimonials */
.testimonials{position:absolute;left:0;top:2104px;width:1200px;height:533px;background:linear-gradient(90deg,#4a7fb2,var(--testi-bg) 60%,#5a8cbd);overflow:hidden}
.testi-title{position:absolute;left:131px;top:112px;font-size:37px;line-height:48px;font-weight:800;color:var(--white)}
.testimonials .btn{left:137px;top:284px;width:202px;height:43px;font-size:13.5px;background:var(--green)}
.arrow{position:absolute;top:381px;width:42px;height:42px;border:2px solid var(--white);border-radius:50%;display:flex;align-items:center;justify-content:center}
.testi-card{position:absolute;top:84px;width:240px;height:380px;background:var(--white)}
.quote-mark{position:absolute;left:30px;top:28px}
.testi-text{position:absolute;left:30px;top:78px;width:200px;font-size:14px;line-height:20.8px;color:#444}
.avatar{position:absolute;left:30px;top:303px;width:50px;height:50px;border-radius:50%;background:linear-gradient(135deg,#7a8fa3,#3e5366)}
.testi-name{position:absolute;left:95px;top:309px;font-size:13.5px;font-weight:700;color:#222}
.testi-place{position:absolute;left:95px;top:329px;font-size:13.5px;color:#444}

/* contact */
.contact{position:absolute;left:0;top:2637px;width:1200px;height:525px;background:var(--light);overflow:hidden}
.contact-title{position:absolute;left:131px;top:56px;font-size:37px;font-weight:700;color:var(--blue)}
.contact-title b{color:var(--green);font-weight:700}
.field{position:absolute;border:1.5px solid var(--steel);background:var(--white);font-size:12px;color:#555;padding:14px 16px}
.contact .btn{left:134px;top:420px;width:119px;height:46px;font-size:17px}

/* footer */
.site-footer{position:absolute;left:0;top:3162px;width:1200px;height:400px;background:var(--footer);color:var(--white)}
.footer-brand{position:absolute;left:135px;top:68px;width:215px;display:flex;flex-direction:column;align-items:center;gap:14px}
.footer-brand .brand-mark{width:72px;height:72px;background:var(--green)}
.footer-brand .brand-name{font-size:27px;color:var(--blue)}
.footer-head{position:absolute;top:61px;font-size:14.5px;font-weight:700}
.footer-head::after{content:"";position:absolute;left:0;top:26px;width:193px;height:2px;background:var(--white)}
.footer-item{position:absolute;left:404px;display:flex;gap:14px;align-items:flex-start;font-size:12.5px;line-height:16px}
.footer-item .dot{width:24px;height:24px;border-radius:50%;background:var(--green);flex:none;margin-top:2px}
.footer-menu{position:absolute;left:677px;top:115px;font-size:13px;line-height:22.4px}
.social{position:absolute;left:909px;top:110px;display:flex;gap:8px}
.social i{width:26px;height:26px;border-radius:50%;background:var(--white)}
.footer-rule{position:absolute;left:138px;top:293px;width:937px;height:1px;background:#444}
.copyright{position:absolute;left:0;top:337px;width:1200px;text-align:center;font-size:12.5px;color:#ddd}
</style>
</head>
<body>

<header class="site-header">
  <div class="brand"><div class="brand-mark"></div><div class="brand-name">Velmora Health</div></div>
  <div class="contact-chip" style="left:607px">
    <div class="chip-icon"><svg width="16" height="12" viewBox="0 0 16 12"><rect x="1" y="1" width="14" height="10" fill="none" stroke="#fff" stroke-width="1.5"/><path d="M1 1l7 6 7-6" fill="none" stroke="#fff" stroke-width="1.5"/></svg></div>
    <div><div class="chip-label">EMAIL US</div><div class="chip-value">info@velmorahealth.com</div></div>
  </div>
  <div class="contact-chip" style="left:894px">
    <div class="chip-icon"><svg width="14" height="14" viewBox="0 0 14 14"><path d="M3 1l2.5 3-1.5 1.5c.8 1.8 2.2 3.2 4 4L9.5 8 13 10.5 11.5 13C6 13 1 8 1 2.5z" fill="#fff"/></svg></div>
    <div><div class="chip-label">CALL US</div><div class="chip-value">+1 868 555 0142</div></div>
  </div>
  <nav class="main-nav">
    <span class="active">HOME</span>
    <span style="margin-left:17px">ABOUT US</span>
    <span style="margin-left:29px">SERVICES</span>
    <span style="margin-left:26px">PATIENT INFORMATION</span>
    <span style="margin-left:29px">RESOURCES</span>
    <span style="margin-left:28px">CONTACT US</span>
  </nav>
</header>

<section class="hero" role="img" aria-label="Doctor in a white coat holding a glowing kidney model above a tablet, bright clinic background">
  <h1 class="hero-title">Hemodialysis<br>Life-Sustaining<br>Treatment</h1>
  <p class="hero-text">Lorem ipsum dolor sit amet consectetur adipiscing<br>elit sed do eiusmod tempor incididun.</p>
  <a class="btn">Read More</a>
  <div class="dots"><i></i><i></i><i></i><i></i></div>
</section>

<section class="mission">
  <svg class="abs" style="left:0;top:80px" width="130" height="95"><polygon points="0,0 0,95 120,95" fill="#5f9646" opacity=".55"/></svg>
  <svg class="abs" style="left:1070px;top:0" width="130" height="90"><polygon points="0,0 130,0 130,90" fill="#5f9646" opacity=".55"/></svg>
  <svg class="abs" style="left:148px;top:58px" width="60" height="58" viewBox="0 0 60 58"><circle cx="28" cy="30" r="25" fill="none" stroke="#fff" stroke-width="4"/><circle cx="28" cy="30" r="16" fill="none" stroke="#fff" stroke-width="4"/><circle cx="28" cy="30" r="7" fill="none" stroke="#fff" stroke-width="4"/><path d="M28 30L52 6M46 4l6 2 2 6" fill="none" stroke="#fff" stroke-width="4" stroke-linecap="round"/></svg>
  <h2 class="mission-title">OUR MISSION</h2>
  <div class="mission-rule"></div>
  <p class="mission-text">Sed ut perspiciatis unde omnis iste natus error sit voluptatem accusantium doloremque laudantium, totam rem aperiam, eaque ipsa quae ab illo inventore veritatis et quasi architecto beatae vitae dicta sunt explicabo. Nemo enim ipsam voluptatem</p>
</section>

<section class="welcome">
  <div class="welcome-media" role="img" aria-label="Clinic image with a hand holding a kidney model, tinted in green and blue"></div>
  <div class="welcome-kicker">WELCOME TO</div>
  <h2 class="welcome-title">VELMORA <b>HEALTH</b></h2>
  <div class="rule" style="left:574px;top:1017px;width:182px"></div>
  <p class="welcome-text">Sed ut perspiciatis unde omnis iste natus error sit voluptatem accusantium doloremque laudantium, totam rem aperiam, eaque ipsa quae ab illo inventore veritatis et quasi architecto beatae vitae dicta sunt explicabo. Nemo enim ipsam voluptatem quia voluptas sit aspernatur aut odit aut fugit, sed quia consequuntur magni dolores eos qui ratione voluptatem sequi nesciunt. Neque porro quisquam est, qui dolorem ipsum quia dolor sit amet, consectetur, adipisci velit, sed quia non numquam eius modi tempora incidunt ut labore et dolore magnam aliquam quaerat.</p>
  <a class="btn">Read More</a>
</section>

<section class="services">
  <h2 class="section-title" style="left:0;width:1200px;text-align:center;top:54px">OUR <b>SERVICES</b></h2>
  <div class="rule" style="left:578px;top:120px;width:44px"></div>

  <div class="service-card" style="left:131px">
    <div class="service-photo" role="img" aria-label="Nurse attending a patient seated beside a dialysis machine" style="background:linear-gradient(135deg,#c9d3dc,#8ea2b3 50%,#d9dde0)"></div>
    <svg width="297" height="485"><defs><linearGradient id="g1" x1="0" x2="1"><stop offset="0" stop-color="#3f7ea6"/><stop offset="1" stop-color="#6aa548"/></linearGradient></defs><polygon points="0,227 297,195 297,485 0,450" fill="#fff"/><line x1="0" y1="224" x2="297" y2="192" stroke="url(#g1)" stroke-width="6"/><line x1="0" y1="448" x2="297" y2="482" stroke="url(#g1)" stroke-width="5"/></svg>
    <div class="service-icon"><svg width="28" height="28" viewBox="0 0 28 28" fill="none" stroke="#fff" stroke-width="2"><rect x="4" y="14" width="20" height="8"/><circle cx="9" cy="9" r="3"/><path d="M16 4h8v8h-8z"/></svg></div>
    <h3 class="service-name">HEMODIALYSIS</h3>
    <p class="service-text">Sed ut perspiciatis unde omnis iste natus error sit voluptatem accusantium dolore mque laudantium, totam rem aperiam, eaque ipsa quae ab illo inventore.</p>
    <a class="btn">Read More</a>
  </div>

  <div class="service-card" style="left:450px">
    <div class="service-photo" role="img" aria-label="Patient resting in a treatment chair while blood pressure is measured" style="background:linear-gradient(135deg,#a84b52,#6d7f96 55%,#c8d0d8)"></div>
    <svg width="297" height="485"><defs><linearGradient id="g2" x1="0" x2="1"><stop offset="0" stop-color="#3f7ea6"/><stop offset="1" stop-color="#6aa548"/></linearGradient></defs><polygon points="0,227 297,195 297,485 0,450" fill="#fff"/><line x1="0" y1="224" x2="297" y2="192" stroke="url(#g2)" stroke-width="6"/><line x1="0" y1="448" x2="297" y2="482" stroke="url(#g2)" stroke-width="5"/></svg>
    <div class="service-icon"><svg width="28" height="28" viewBox="0 0 28 28" fill="none" stroke="#fff" stroke-width="2"><rect x="5" y="4" width="9" height="18"/><path d="M7 8h5M7 12h5M8 25h3"/><circle cx="20" cy="9" r="2.5"/><path d="M17 24v-9h6v9"/></svg></div>
    <h3 class="service-name">PERITONEAL DIALYSIS</h3>
    <p class="service-text">Sed ut perspiciatis unde omnis iste natus error sit voluptatem accusantium dolore mque laudantium, totam rem aperiam, eaque ipsa quae ab illo inventore.</p>
    <a class="btn">Read More</a>
  </div>

  <div class="service-card" style="left:771px">
    <div class="service-photo" role="img" aria-label="Patient seated in a home treatment chair next to a dialysis unit" style="background:linear-gradient(135deg,#d9dcd8,#9aa8b2 50%,#e4e4e0)"></div>
    <svg width="297" height="485"><defs><linearGradient id="g3" x1="0" x2="1"><stop offset="0" stop-color="#3f7ea6"/><stop offset="1" stop-color="#6aa548"/></linearGradient></defs><polygon points="0,227 297,195 297,485 0,450" fill="#fff"/><line x1="0" y1="224" x2="297" y2="192" stroke="url(#g3)" stroke-width="6"/><line x1="0" y1="448" x2="297" y2="482" stroke="url(#g3)" stroke-width="5"/></svg>
    <div class="service-icon" style="left:190px;top:170px;width:64px;height:64px"><svg width="30" height="28" viewBox="0 0 30 28"><path d="M15 2L2 14h4v12h7v-8h4v8h7V14h4z" fill="#fff"/></svg></div>
    <h3 class="service-name">HOME HEMODIALYSIS</h3>
    <p class="service-text">Sed ut perspiciatis unde omnis iste natus error sit voluptatem accusantium dolore mque laudantium, totam rem aperiam, eaque ipsa quae ab illo inventore.</p>
    <a class="btn">Read More</a>
  </div>
</section>

<section class="testimonials" role="img" aria-label="Blue-tinted background of a dialysis ward">
  <h2 class="testi-title">CUTOMER<br>TESTIMONIALS</h2>
  <div class="rule" style="left:135px;top:238px;width:43px;background:#fff"></div>
  <a class="btn">View All Testimonials</a>
  <div class="arrow" style="left:135px"><svg width="12" height="16"><path d="M9 2L3 8l6 6" fill="none" stroke="#fff" stroke-width="2"/></svg></div>
  <div class="arrow" style="left:197px"><svg width="12" height="16"><path d="M3 2l6 6-6 6" fill="none" stroke="#fff" stroke-width="2"/></svg></div>

  <div class="testi-card" style="left:453px">
    <svg class="quote-mark" width="28" height="24"><path d="M0 24V12C0 5 4 1 11 0v4c-4 1-6 4-6 8h6v12zM16 24V12c0-7 4-11 11-12v4c-4 1-6 4-6 8h6v12z" fill="#4f8a6e"/></svg>
    <p class="testi-text">Sed ut perspiciatis unde omni s iste natus error sit volup tatem accusantium dol oremque laudantium, totam rem aperi am, eaque ipsa quae ab illo inventore verit atis et quasi architecto beatae vitae dicta sunt exp licabo. Nemo enim ipsam voluptatem.</p>
    <div class="avatar" role="img" aria-label="Customer portrait"></div>
    <div class="testi-name">DANIEL</div><div class="testi-place">Scarborough</div>
  </div>
  <div class="testi-card" style="left:712px">
    <svg class="quote-mark" width="28" height="24"><path d="M0 24V12C0 5 4 1 11 0v4c-4 1-6 4-6 8h6v12zM16 24V12c0-7 4-11 11-12v4c-4 1-6 4-6 8h6v12z" fill="#4f8a6e"/></svg>
    <p class="testi-text">Sed ut perspiciatis unde omni s iste natus error sit volup tatem accusantium dol oremque laudantium, totam rem aperi am, eaque ipsa quae ab illo inventore verit atis et quasi architecto beatae vitae dicta sunt exp licabo. Nemo enim ipsam voluptatem.</p>
    <div class="avatar" role="img" aria-label="Customer portrait"></div>
    <div class="testi-name">DANIEL</div><div class="testi-place">Scarborough</div>
  </div>
  <div class="testi-card" style="left:972px">
    <svg class="quote-mark" width="28" height="24"><path d="M0 24V12C0 5 4 1 11 0v4c-4 1-6 4-6 8h6v12zM16 24V12c0-7 4-11 11-12v4c-4 1-6 4-6 8h6v12z" fill="#4f8a6e"/></svg>
    <p class="testi-text">Sed ut perspiciatis unde omni s iste natus error sit volup tatem accusantium dol oremque laudantium, totam rem aperi am, eaque ipsa quae ab illo inventore verit atis et quasi architecto beatae vitae dicta sunt exp licabo. Nemo enim ipsam voluptatem.</p>
    <div class="avatar" role="img" aria-label="Customer portrait"></div>
    <div class="testi-name">DANIEL</div><div class="testi-place">Scarborough</div>
  </div>
</section>

<section class="contact">
  <svg class="abs" style="left:0;top:0" width="1200" height="525">
    <polygon points="586,0 1200,0 1200,525 640,525" fill="#3f76ad"/>
  </svg>
  <div class="abs" role="img" aria-label="Nurse connecting a seated patient to a dialysis machine in a bright ward" style="left:0;top:0;width:1200px;height:525px;clip-path:polygon(608px 0,1200px 0,1200px 525px,650px 525px);background:linear-gradient(135deg,#e9ecee,#b9c7cf 45%,#dfe3e4 75%,#cfd7dc)"></div>
  <h2 class="contact-title">CONTACT <b>US</b></h2>
  <div class="rule" style="left:134px;top:120px;width:44px"></div>
  <div class="field" style="left:134px;top:158px;width:200px;height:43px">First Name</div>
  <div class="field" style="left:350px;top:158px;width:200px;height:43px">Last Name</div>
  <div class="field" style="left:134px;top:214px;width:200px;height:43px">Email id</div>
  <div class="field" style="left:350px;top:214px;width:200px;height:43px">Phone</div>
  <div class="field" style="left:134px;top:269px;width:416px;height:125px">Message</div>
  <a class="btn">Submit</a>
</section>

<footer class="site-footer">
  <div class="footer-brand"><div class="brand-mark"></div><div class="brand-name">Velmora Health</div></div>

  <div class="footer-head" style="left:404px">CONTACT US</div>
  <div class="footer-item" style="top:115px"><span class="dot"></span><span>14 Shore Road,<br>Mt. Irvine</span></div>
  <div class="footer-item" style="top:165px"><span class="dot"></span><span>Call Us<br>+1 868 555 0142</span></div>
  <div class="footer-item" style="top:216px"><span class="dot"></span><span>E mail Us<br>info@VelmoraHealth.com</span></div>

  <div class="footer-head" style="left:677px">MENU</div>
  <div class="footer-menu">Home<br>About Us<br>Services<br>Patient Information<br>Resources<br>Contact Us</div>

  <div class="footer-head" style="left:908px">FOLLOW US</div>
  <div class="social"><i></i><i></i><i></i><i></i></div>

  <div class="footer-rule"></div>
  <div class="copyright">Copyright © 2024 All Rights Reserved</div>
</footer>

</body>
</html>
```